Leaflets
We supply stone and solid surfaces to the trade and project manage its installation
Project: Leaflets
Leaflets - Construction
Creative Brief
Construction
Architects, Interior designers, property developers, kitchen and bathroom designers, shopfitters Our offer is mainly business to business. Our branding and images are corporate and our content (wording) is more casual (which is what makes us different from the competition)
A leaflet with our branding, logos and fonts to be used as an introduction to our clients mainly targeted trough site visits and by posting samples. Images and branding available on request.

```html
<!DOCTYPE html>
<html lang="en">
<head>
<meta charset="utf-8">
<title>Trelvax Surfaces – Trade Leaflet</title>
<link href="https://fonts.googleapis.com/css2?family=Open+Sans:wght@400;600;700&display=swap" rel="stylesheet">
<style>
  :root {
    --stage: #3b3b3d;
    --paper: #f4f4f4;
    --paper-edge: #e2e2e2;
    --ink: #5a5a5a;
    --ink-soft: #7a7a7a;
    --accent-green: #8dc63f;
    --accent-purple: #6a3d8f;
    --photo-cool: #c9ced2;
    --photo-warm: #b9b2a8;
    --photo-teal: #3fb3c8;
  }
  * { box-sizing: border-box; margin: 0; padding: 0; }
  html, body { width: 1200px; height: 866px; overflow: hidden; }
  body {
    background: var(--stage);
    font-family: "Open Sans", Arial, sans-serif;
    display: flex; align-items: center; justify-content: center;
  }
  .leaflet-spread {
    width: 1140px; height: 806px;
    display: grid; grid-template-columns: repeat(3, 1fr);
    background: var(--paper);
  }
  .panel {
    position: relative;
    padding: 0 0 28px;
    border-right: 1px solid var(--paper-edge);
    display: flex; flex-direction: column;
  }
  .panel:last-child { border-right: none; }
  .photo { width: 100%; flex: none; }
  .photo--stair { height: 200px; background: linear-gradient(135deg, var(--photo-cool), #eef0f1 55%, var(--photo-teal)); }
  .photo--interior { height: 170px; background: linear-gradient(160deg, #8e9599, var(--photo-cool) 60%, #e6e6e6); }
  .photo--kitchen { height: 190px; background: linear-gradient(180deg, #d8d6d2, var(--photo-warm) 60%, #6d6660); }
  .photo--showroom { height: 170px; background: linear-gradient(150deg, #e8e8e6, var(--photo-cool) 50%, #9a9187); }
  .section-heading {
    margin: 22px 0 16px;
    width: 62%;
    background: var(--accent-green);
    color: #fff;
    font-size: 13px; font-weight: 600;
    padding: 6px 26px;
  }
  .copy { padding: 0 28px; }
  .copy p {
    color: var(--ink);
    font-size: 11.5px; line-height: 1.65;
    margin-bottom: 12px;
    text-align: justify;
  }
  .panel--intro .copy { padding-top: 26px; }
  .panel--services .photo--kitchen { margin-top: auto; }
  .contact-block {
    margin-top: auto;
    padding: 0 28px;
    text-align: right;
    color: var(--ink-soft);
    font-size: 11px; line-height: 1.6;
  }
  .brand {
    display: inline-flex; align-items: center; gap: 8px;
    margin-bottom: 12px;
  }
  .brand-mark { width: 16px; height: 16px; background: var(--accent-purple); }
  .brand-name { font-size: 22px; font-weight: 700; color: var(--accent-purple); }
</style>
</head>
<body>
  <main class="leaflet-spread">
    <section class="panel panel--intro">
      <div class="photo photo--stair" role="img" aria-label="Photo of a glass staircase beside an indoor pool"></div>
      <div class="copy">
        <p>At Trelvax Surfaces we supply natural stone and solid surfaces to the trade, and we look after the whole job from template to final fit. We keep things simple, friendly and on time.</p>
        <p>Our team works with architects, interior designers, developers, shopfitters and kitchen and bathroom designers on projects of every size, from a single vanity top to a full residential block.</p>
        <p>We talk to you like people, not like a catalogue. Tell us what you need and we will find the right material, the right finish and the right price for it.</p>
        <p>Every project gets one named contact who follows it from the first sample to the last joint, so you always know who to call.</p>
      </div>
    </section>

    <section class="panel panel--services">
      <div class="photo photo--interior" role="img" aria-label="Photo of a modern interior with stone flooring"></div>
      <h2 class="section-heading">What we do</h2>
      <div class="copy">
        <p>We source quartz, granite, marble and solid surfaces from trusted mills and fabricate them in our own workshop.</p>
        <p>Our fitters install worktops, vanities, wall cladding, reception desks and bespoke pieces with clean joints and tidy edges.</p>
        <p>We manage the programme on site, coordinate with other trades and leave the space ready to hand over.</p>
      </div>
      <div class="photo photo--kitchen" role="img" aria-label="Photo of a kitchen with stone worktops and island"></div>
    </section>

    <section class="panel panel--contact">
      <div class="photo photo--showroom" role="img" aria-label="Photo of a bright kitchen showroom"></div>
      <h2 class="section-heading">Why work with us</h2>
      <div class="copy">
        <p>Honest advice, fair prices and samples sent to your door within days.</p>
        <p>A project manager on every job, a workshop you can visit and a team that answers the phone.</p>
      </div>
      <address class="contact-block" style="font-style:normal">
        <div class="brand"><span class="brand-mark"></span><span class="brand-name">Trelvax</span></div><br>
        Trelvax Surfaces<br>
        27 Fenwick Yard<br>
        London, N4 2PQ<br><br>
        Tel: 020 0000 0000<br>
        Email: hello@trelvax-surfaces.example
      </address>
    </section>
  </main>
</body>
</html>
```